Asphalt Driveway Billboard Design

We need a billboard designed for an Asphalt & Concrete Company in Minnesota. We want to advertise Asphalt Driveways on this billboard! Logo is uploaded below. Our website is tamlin-paving.com for more information.

```html
<!DOCTYPE html>
<html lang="en">
<head>
<meta charset="utf-8">
<title>Tamlin Paving &amp; Concrete – Billboard</title>
<link href="https://fonts.googleapis.com/css2?family=Montserrat:wght@400;600;700;800&display=swap" rel="stylesheet">
<style>
  :root {
    --page-bg: #d6d6d6;
    --board-white: #ffffff;
    --brand-blue: #0a6cc4;
    --ink-dark: #1c1c1c;
    --panel-grey: #5a5a5a;
    --text-white: #ffffff;
  }
  * { margin: 0; padding: 0; box-sizing: border-box; }
  html, body {
    width: 1092px; height: 1200px; overflow: hidden;
    background: var(--page-bg);
    font-family: "Montserrat", Arial, sans-serif;
  }
  .billboard {
    position: absolute; left: 46px; top: 381px;
    width: 1000px; height: 437px;
    background: var(--board-white);
    box-shadow: 10px 14px 22px rgba(0,0,0,0.35);
    overflow: hidden;
  }
  .billboard-art { position: absolute; inset: 0; width: 1000px; height: 437px; }
  .brand {
    position: absolute; right: 46px; top: 48px;
    display: flex; align-items: center; gap: 12px;
  }
  .brand-dot { width: 26px; height: 26px; border-radius: 50%; background: var(--brand-blue); }
  .brand-name {
    font-size: 25px; font-weight: 800; color: var(--ink-dark);
    letter-spacing: 0.5px; white-space: nowrap;
  }
  .headline {
    position: absolute; left: 560px; width: 430px; text-align: center;
    font-weight: 800; white-space: nowrap;
  }
  .headline-lead { top: 140px; font-size: 28px; color: var(--brand-blue); }
  .headline-main { top: 178px; font-size: 28px; color: var(--ink-dark); }
  .tagline {
    position: absolute; left: 560px; width: 430px; top: 210px; text-align: center;
    font-size: 16px; font-weight: 400; color: var(--ink-dark); white-space: nowrap;
  }
  .contact {
    position: absolute; right: 37px; top: 332px; text-align: right;
    color: var(--text-white); line-height: 1;
  }
  .contact-offer { font-size: 19px; font-weight: 700; }
  .contact-phone { font-size: 29px; font-weight: 800; margin-top: 7px; }
  .contact-web { font-size: 22px; font-weight: 400; margin-top: 8px; }
  .contact-web strong { font-weight: 700; }
</style>
</head>
<body>
  <div class="billboard">
    <svg class="billboard-art" viewBox="0 0 1000 437" xmlns="http://www.w3.org/2000/svg">
      <defs>
        <linearGradient id="driveway-photo" x1="0" y1="0" x2="0" y2="1">
          <stop offset="0" stop-color="#8fb4d8"/>
          <stop offset="0.25" stop-color="#c9c9c6"/>
          <stop offset="0.5" stop-color="#d9d9d6"/>
          <stop offset="0.6" stop-color="#6d8a4a"/>
          <stop offset="0.66" stop-color="#3d3f45"/>
          <stop offset="1" stop-color="#35373c"/>
        </linearGradient>
      </defs>
      <path class="side-band" fill="#0a6cc4"
        d="M0,0 L428,0 C520,70 575,175 552,265 C538,340 520,400 512,437 L0,437 Z"/>
      <path class="driveway-photo" role="img" aria-label="Photo of a two-storey house with white garage doors and a freshly paved black asphalt driveway"
        fill="url(#driveway-photo)" stroke="#ffffff" stroke-width="6"
        d="M-4,-4 L414,-4 C470,60 502,160 495,245 C488,330 432,400 380,441 L-4,441 Z"/>
      <path class="footer-band" fill="#0a6cc4"
        d="M500,437 C590,320 740,262 1000,250 L1000,437 Z"/>
      <path class="footer-panel" fill="#5a5a5a" stroke="#ffffff" stroke-width="4"
        d="M530,441 C615,348 770,300 1004,300 L1004,441 Z"/>
    </svg>

    <div class="brand">
      <span class="brand-dot"></span>
      <span class="brand-name">TAMLIN PAVING &amp; CONCRETE</span>
    </div>

    <div class="headline headline-lead">YOU DESERVE TO</div>
    <div class="headline headline-main">COME HOME TO QUALITY</div>
    <div class="tagline">We’re here to help you smooth things over.</div>

    <div class="contact">
      <div class="contact-offer">GET A FREE ESTIMATE</div>
      <div class="contact-phone">CALL: (763) 555-0148</div>
      <div class="contact-web">www.<strong>tamlin-paving</strong>.com</div>
    </div>
  </div>
</body>
</html>
```